Granite Ridge College-Pinecrest Welcome Week

I am the Student Activities Coordinator at Granite Ridge College-Pinecrest. For Welcome Week 2013, I need a standard poster 24x36 with the list of events happening. Our theme is based on the popular Friday Late Laughs video "We Got a Kite"
http://www.vidtrove.example/clip/Q4mZp8sLwTe
Our theme is:
We're at the 'Crest!
Welcome Week 2013
Graphics on the poster should reflect popular images/designs of FLL We Got a Kite. However, the boat should be a steamboat instead of the yacht image.
Unfortunately, I have a lot of text to fit on the poster. Traditionally we go with 3 margins listing events. I'm attaching the word document of events and our logo to this proposal. I'll also attach a few google images of "We Got a Kite" that align with the type of theme I'm looking for.
One last thing, our logo contains mountains listing all of the different campuses. Remove the campus names and mountains all together. Use simply the Colorado flag C and "Granite Ridge College".
Thanks for considering this brief!
Glen
Target Market(s)
Our college students love to ski and snowboard. In fact, one of our degrees is "Alpine Slope Commerce". Their ages are 18-22.
Industry/Entity Type
Events
Look and feel

```html
<!DOCTYPE html>
<html lang="en">
<head>
<meta charset="utf-8">
<title>Granite Ridge College Welcome Week 2013</title>
<link rel="stylesheet" href="https://fonts.googleapis.com/css2?family=Anton&family=Open+Sans:wght@400;700&family=Playfair+Display:ital,wght@1,900&display=swap">
<style>
:root{
  --navy:#29306b;
  --navy-text:#2b3472;
  --band:#d3d5e4;
  --mid-head:#b3b8dc;
  --yellow:#f5ec3a;
  --red:#e8141b;
  --ink:#2e2e2e;
  --page:#e6e6e8;
}
*{margin:0;padding:0;box-sizing:border-box}
html,body{width:1186px;height:1200px;overflow:hidden;background:var(--page)}
.poster{position:absolute;left:243px;top:75px;width:700px;height:1050px;background:var(--navy);overflow:hidden;font-family:"Open Sans",sans-serif}
.backdrop{position:absolute;inset:0}
.abs{position:absolute;white-space:nowrap}
.college{left:180px;top:26px;font-size:20px;letter-spacing:7px;color:var(--yellow)}
.title{font-family:"Anton",sans-serif;color:var(--yellow);font-size:44px;line-height:1;text-transform:uppercase}
.title-1{left:180px;top:55px}
.title-2{left:180px;top:112px}
.year{left:335px;top:135px;font-family:"Playfair Display",serif;font-style:italic;font-weight:900;font-size:82px;color:var(--red);transform:rotate(-14deg);transform-origin:left bottom;-webkit-text-stroke:1px var(--yellow)}
.join{left:448px;top:215px;width:150px;height:150px}
.join-text{left:448px;width:150px;text-align:center;color:var(--yellow);font-family:"Anton",sans-serif}
.join-main{top:240px;font-size:26px;-webkit-text-stroke:0.5px #000}
.join-sub{top:276px;font-size:10px;color:#111}
.join-sub b{color:#fff;font-weight:400}
.col-white{position:absolute;background:#fff}
.col-mid{position:absolute;left:268px;top:370px;width:222px;height:668px;background:var(--navy)}
.band{position:absolute;left:0;width:268px;height:26px;background:var(--band)}
.band-r{left:490px;width:210px}
.head{font-family:"Anton",sans-serif;font-size:20px;color:var(--navy-text);line-height:26px}
.date{font-family:"Anton",sans-serif;font-size:27px;color:var(--navy-text);line-height:30px}
.date small{font-size:18px}
.mid .head{color:var(--mid-head)}
.mid .date{color:#fff}
.line{font-size:14px;color:var(--ink);line-height:19px}
.on-photo .line{color:#111}
.mid .line{color:#fff}
.line .tiny{font-size:10px}
.line.strong{font-weight:700}
.arrow{left:0;top:248px}
.footer{position:absolute;top:1015px;height:35px;background:var(--red);font-family:"Anton",sans-serif;font-size:19px;line-height:35px;text-align:center}
.footer-left{left:0;width:268px;color:var(--navy)}
.footer-left span{color:var(--yellow)}
.footer-right{left:490px;width:210px;color:#fff}
.footer-mid{left:268px;width:222px;top:1038px;height:12px}
</style>
</head>
<body>
<main class="poster">
  <svg class="backdrop" width="700" height="1050" viewBox="0 0 700 1050">
    <path d="M0 190 C130 160 250 170 350 205 L350 470 L0 470 Z" fill="#7fb3d6" role="img" aria-label="Photo of a blue sky over a sunny beach and sea"/>
    <path d="M350 80 C450 90 600 70 700 60 L700 360 L350 360 Z" fill="#b9bdd6" role="img" aria-label="Photo of a steamboat with a man standing arms raised on the bow"/>
    <circle cx="120" cy="88" r="48" fill="var(--yellow)"/>
  </svg>

  <div class="col-white" style="left:0;top:440px;width:268px;height:575px"></div>
  <svg class="abs" style="left:0;top:395px" width="268" height="60" viewBox="0 0 268 60"><path d="M0 60 L0 55 C90 40 180 20 268 40 L268 60 Z" fill="#fff"/></svg>
  <div class="col-white" style="left:490px;top:360px;width:210px;height:655px"></div>
  <div class="col-mid"></div>

  <p class="abs college">Granite Ridge College</p>
  <h1 class="abs title title-1">We're at the 'Crest!</h1>
  <p class="abs title title-2">Welcome Week</p>
  <p class="abs year">2013</p>

  <svg class="abs join" viewBox="0 0 150 150">
    <polygon fill="var(--red)" points="75,2 86,22 106,8 109,31 132,25 126,48 148,52 133,70 148,88 127,95 133,118 110,114 106,137 87,125 75,148 63,125 44,137 40,114 17,118 23,95 2,88 17,70 2,52 24,48 18,25 41,31 44,8 64,22"/>
  </svg>
  <p class="abs join-text join-main">Join Us</p>
  <p class="abs join-text join-sub">ALL EVENTS ARE <b>FREE</b></p>

  <svg class="abs arrow" width="22" height="60" viewBox="0 0 22 60"><polygon points="0,0 22,30 0,60 0,48 12,30 0,12" fill="var(--yellow)"/></svg>

  <section class="on-photo">
    <h2 class="abs date" style="left:25px;top:263px">Thursday Aug 22</h2>
    <p class="abs line" style="left:28px;top:302px">Residence Hall Move-In</p>
    <p class="abs line" style="left:28px;top:321px">12:00pm-3:00pm</p>
    <p class="abs line" style="left:28px;top:340px">Summit Hall</p>
    <h3 class="abs head" style="left:25px;top:370px">Brunch</h3>
    <p class="abs line" style="left:28px;top:398px">10:00am-1:00pm</p>
    <p class="abs line" style="left:28px;top:417px">Dining Hall</p>
  </section>

  <section class="left">
    <div class="band" style="top:458px"></div><h3 class="abs head" style="left:25px;top:458px">International Students</h3>
    <p class="abs line" style="left:28px;top:484px">Orientation 3:00pm</p>
    <p class="abs line" style="left:28px;top:503px">Carver 121</p>
    <div class="band" style="top:533px"></div><h3 class="abs head" style="left:25px;top:533px">Hot Springs Waterslide Party</h3>
    <p class="abs line" style="left:28px;top:558px">7:00pm-9:00pm</p>
    <p class="abs line" style="left:28px;top:577px">Old Mill Hot Springs</p>
    <h2 class="abs date" style="left:25px;top:606px">Friday Aug 23</h2>
    <p class="abs line" style="left:28px;top:638px">Breakfast 7:30am-9:00am</p>
    <p class="abs line" style="left:28px;top:657px">Dining Hall</p>
    <div class="band" style="top:686px"></div><h3 class="abs head" style="left:25px;top:686px">Hike Cedar Run Falls</h3>
    <p class="abs line" style="left:28px;top:711px">9:00am-11:30am</p>
    <p class="abs line" style="left:28px;top:730px">Shuttle leaves Summit Hall at 8:30am</p>
    <div class="band" style="top:763px"></div><h3 class="abs head" style="left:25px;top:763px">BBQ and Faculty Ice Cream</h3>
    <p class="abs line" style="left:28px;top:789px">Social 12:00pm-1:30pm</p>
    <p class="abs line" style="left:28px;top:808px">Dining Hall</p>
    <div class="band" style="top:838px"></div><h3 class="abs head" style="left:25px;top:838px">Kick Off Party: Inflatables</h3>
    <p class="abs line" style="left:28px;top:865px">1:30pm-4:00pm&nbsp; Upper Parking Lot</p>
    <div class="band" style="top:896px"></div><h3 class="abs head" style="left:25px;top:896px">Dinner</h3>
    <p class="abs line" style="left:28px;top:921px">5:00pm-6:00pm&nbsp; Dining Hall</p>
    <div class="band" style="top:951px"></div><h3 class="abs head" style="left:25px;top:951px">Free Concert</h3>
    <p class="abs line" style="left:28px;top:978px">7:00pm&nbsp; Pinecrest Resort Base</p>
    <p class="abs line" style="left:28px;top:995px"><span class="tiny">(PRT Buses to Resort, 5:35pm Last Bus)</span></p>
  </section>

  <section class="mid">
    <h2 class="abs date" style="left:282px;top:368px">Saturday Aug 24</h2>
    <p class="abs line" style="left:284px;top:400px">Main Street Farmers Market</p>
    <p class="abs line" style="left:284px;top:420px">9:00am-2:00pm</p>
    <p class="abs line" style="left:284px;top:440px">4th &amp; Aspen <span class="tiny">(walking dist.)</span></p>
    <h3 class="abs head" style="left:282px;top:466px">Brunch</h3>
    <p class="abs line" style="left:286px;top:492px">10:00am-1:00pm Dining Hall</p>
    <h3 class="abs head" style="left:282px;top:517px">Bramble Park</h3>
    <h3 class="abs head" style="left:282px;top:541px">Hot Springs</h3>
    <p class="abs line" style="left:286px;top:568px">2:00pm-5:00pm Shuttle leaves</p>
    <p class="abs line" style="left:286px;top:588px">Summit Hall at 1:30pm</p>
    <h3 class="abs head" style="left:282px;top:618px">Dinner</h3>
    <p class="abs line" style="left:286px;top:643px">5:00-6:00pm&nbsp; Dining Hall</p>
    <h3 class="abs head" style="left:282px;top:674px">Free Movie on Mountain</h3>
    <p class="abs line" style="left:286px;top:700px">Arena Trials 8:00pm</p>
    <p class="abs line" style="left:286px;top:717px"><span class="tiny">(PRT Buses to Resort, 5:35pm Last Bus)</span></p>
    <h2 class="abs date" style="left:282px;top:750px">Sunday Aug 25</h2>
    <p class="abs line" style="left:286px;top:781px">Brunch 10:00am-1:00pm</p>
    <p class="abs line" style="left:286px;top:801px">Dining Hall</p>
    <h3 class="abs head" style="left:282px;top:828px">Alpine Slide/Volleyball</h3>
    <p class="abs line" style="left:286px;top:856px">2:00pm-4:00pm</p>
    <p class="abs line" style="left:286px;top:876px">Meet at Larkin Hill</p>
    <h3 class="abs head" style="left:282px;top:904px">Dinner</h3>
    <p class="abs line" style="left:286px;top:931px">5:00pm-6:00pm Dining Hall</p>
    <h3 class="abs head" style="left:282px;top:956px">Mandatory All Hall</h3>
    <h3 class="abs head" style="left:282px;top:980px">Meeting</h3>
    <p class="abs line" style="left:286px;top:1008px">6:00pm&nbsp; Auditorium</p>
  </section>

  <section class="right">
    <div class="band band-r" style="top:383px"></div>
    <h3 class="abs head" style="left:505px;top:383px">RHA Super Sunday <span style="font-size:11px">Program</span></h3>
    <p class="abs line" style="left:507px;top:408px">8:00pm Summit Hall: MPR</p>
    <h2 class="abs date" style="left:505px;top:440px">Monday Aug 23</h2>
    <p class="abs line" style="left:507px;top:471px">Regular Dining Hall</p>
    <p class="abs line" style="left:507px;top:490px">Hours Begin</p>
    <p class="abs line" style="left:507px;top:510px">“Being Alone Sucks!”</p>
    <p class="abs line" style="left:507px;top:529px">9:00pm Auditorium</p>
    <h2 class="abs date" style="left:505px;top:564px">Tuesday Aug 23</h2>
    <p class="abs line" style="left:507px;top:595px">Newly Roommate Game</p>
    <p class="abs line" style="left:507px;top:614px">7:00pm-8:00pm</p>
    <p class="abs line" style="left:507px;top:634px">Summit Hall: MPR</p>
    <p class="abs line strong" style="left:507px;top:653px">Free Gelato</p>
    <p class="abs line" style="left:507px;top:673px">8:00pm-9:00pm</p>
    <p class="abs line" style="left:507px;top:692px">Dolce Cone 5th and Birch</p>
    <h2 class="abs date" style="left:505px;top:722px">Wednesday <small>Aug 23</small></h2>
    <p class="abs line" style="left:507px;top:753px">Free Bowling</p>
    <p class="abs line" style="left:507px;top:773px">9:00pm Alpine Lanes</p>
    <h2 class="abs date" style="left:505px;top:799px">Thursday <small>Aug 23</small></h2>
    <p class="abs line" style="left:507px;top:831px">Club Fair 10:00am-2:00pm</p>
    <p class="abs line" style="left:507px;top:850px">Dining Hall</p>
    <p class="abs line strong" style="left:507px;top:870px">Black Light Dodgeball</p>
    <p class="abs line" style="left:507px;top:889px">9:00pm Gym</p>
    <h2 class="abs date" style="left:505px;top:923px">Friday&nbsp; <small>Aug 23</small></h2>
    <p class="abs line" style="left:507px;top:955px">Late Night Climbing</p>
    <p class="abs line" style="left:507px;top:974px">9:00pm Gym</p>
  </section>

  <p class="footer footer-left">ALL EVENTS ARE <span>FREE</span></p>
  <div class="footer footer-mid"></div>
  <p class="footer footer-right">UNLESS OTHERWISE NOTED</p>
</main>
</body>
</html>
```